Tallow Bright business card

Tallow Bright is a new online life insurance company providing instant quotes and policies to consumers.
Target Market(s)
Target market is both business to business as well as business to consumer
Can think out side of the box- We are an open minded bunch
Industry/Entity Type
Life Insurance
Requirements
Must have
- Our corporate Logo
Double sided
Website www.tallowbright.com.au
Phone Number
Name & Position of each person etc.
Modern font

```html
<!DOCTYPE html>
<html lang="en">
<head>
<meta charset="utf-8">
<title>Tallow Bright business card</title>
<link href="https://fonts.googleapis.com/css2?family=Questrial&family=Montserrat:wght@700&display=swap" rel="stylesheet">
<style>
  :root {
    --page: #ffffff;
    --card-top: #7c7c7c;
    --card-mid: #a6a6a6;
    --card-bottom: #8a8a8a;
    --ink: #161616;
    --orange: #f47b20;
    --band: #0d0d0d;
  }
  * { margin: 0; padding: 0; box-sizing: border-box; }
  html, body {
    width: 1200px; height: 355px; overflow: hidden;
    background: var(--page);
    font-family: "Questrial", sans-serif;
  }
  .sheet { position: relative; width: 1200px; height: 355px; }
  .card {
    position: absolute; top: 13px;
    width: 575px; height: 327px;
    border-radius: 18px; overflow: hidden;
    background: linear-gradient(170deg, var(--card-top) 0%, var(--card-mid) 45%, var(--card-bottom) 100%);
  }
  .card--front { left: 16px; }
  .card--back { left: 608px; }
  .band {
    position: absolute; left: 0; right: 0; bottom: 0; height: 30px;
    background: var(--band);
    color: var(--orange);
    display: flex; align-items: center; justify-content: center;
    font-size: 15px;
  }
  .card--front .band { letter-spacing: 4px; }
  .card--back .band { letter-spacing: 2px; font-size: 16px; }
  .band-rule {
    position: absolute; right: 0; bottom: 30px; width: 62%; height: 2px;
    background: var(--orange);
  }
  .brand {
    position: absolute; color: var(--ink); line-height: 0.9;
    font-family: "Questrial", sans-serif;
  }
  .card--front .brand { left: 84px; top: 58px; font-size: 100px; }
  .card--back .brand { left: 52px; top: 108px; font-size: 42px; }
  .divider {
    position: absolute; left: 271px; top: 112px; width: 1px; height: 82px;
    background: var(--orange);
  }
  .person { position: absolute; left: 311px; top: 123px; }
  .person-name {
    font-family: "Montserrat", sans-serif; font-weight: 700;
    color: var(--orange); font-size: 18px; letter-spacing: 0.5px;
  }
  .person-role {
    text-align: right; font-size: 10px; color: var(--ink);
    font-weight: 700; margin-top: -2px; padding-right: 3px;
  }
  .contacts { position: absolute; left: 311px; top: 166px; list-style: none; }
  .contacts li {
    display: flex; align-items: center; gap: 6px;
    font-size: 11px; color: var(--ink); height: 14px;
  }
  .contacts svg { width: 10px; height: 10px; fill: var(--ink); }
</style>
</head>
<body>
<div class="sheet">
  <section class="card card--front">
    <div class="brand">Tallow<br>Bright</div>
    <div class="band">www.tallowbright.com.au</div>
  </section>

  <section class="card card--back">
    <div class="brand">Tallow<br>Bright</div>
    <div class="divider"></div>
    <div class="person">
      <div class="person-name">YOUR NAME....</div>
      <div class="person-role">POSITION</div>
    </div>
    <ul class="contacts">
      <li><svg viewBox="0 0 10 10"><path d="M1 3 Q5 0 9 3 L8 4.5 L6.5 4 L6.5 3 Q5 2.5 3.5 3 L3.5 4 L2 4.5 Z M2 5 H8 V9 H2 Z"/></svg>00 0000 0000</li>
      <li><svg viewBox="0 0 10 10"><path d="M0 2 H10 V8 H0 Z M0.8 2.6 L5 5.6 L9.2 2.6 Z" fill-rule="evenodd"/></svg>XXXX@TALLOWBRIGHT.COM.AU</li>
      <li><svg viewBox="0 0 10 10"><path d="M5 0.5 A4.5 4.5 0 1 0 5 9.5 A4.5 4.5 0 1 0 5 0.5 Z M5 2 A3 3 0 1 1 5 8 A3 3 0 1 1 5 2 Z M2.5 4.5 H7.5 V5.5 H2.5 Z" fill-rule="evenodd"/></svg>WWW.TALLOWBRIGHT.COM.AU</li>
    </ul>
    <div class="band-rule"></div>
    <div class="band">WWW.TALLOWBRIGHT.COM.AU</div>
  </section>
</div>
</body>
</html>
```